QLDR Individual and Corporate Development Business Card Design

QLDR needs a business card design that is aligned with it's values and targetted markets. Harmonic Ladder of Reasoning Matrix's self diagnosis model and tools, which can be used for personal improvement and team/business performance enhancement, is based on the learnings of over 20 years of medical practitioning. QLDR supercharges personal effectiveness and awareness to also increase team and business performance.

The targetted markets are high performance individuals and teams who aspire seek to enhance their capabilities and achieve their absolute best potential.

Look and feel for the business card design we are looking for is high technology, premium, fresh, new and medical.

Target Market(s)

Industry/Entity Type

Business Consultant

Contact Information for Business Card

Logo, Full Name, Title, Phone number, Email, company name, Address,

Font styles to use
Sans Serif

Requirements
Must have
• Tag line: Elevating Clarity for Purposeful Focused Leaders
• Please use same colours as the logo.

```html
<!DOCTYPE html>
<html lang="en">
<head>
<meta charset="utf-8">
<title>QLDR Business Card</title>
<link rel="stylesheet" href="https://fonts.googleapis.com/css2?family=Roboto:wght@400;500;700&display=swap">
<style>
  :root {
    --backdrop: #2f2b29;
    --card: #1c1e20;
    --teal: #1ba7c1;
    --muted: #63686c;
    --text-soft: #7a8085;
  }
  * { margin: 0; padding: 0; box-sizing: border-box; }
  html, body { width: 1200px; height: 780px; overflow: hidden; }
  body {
    background: var(--backdrop);
    font-family: "Roboto", Arial, sans-serif;
    position: relative;
  }
  .card {
    position: absolute;
    width: 540px;
    height: 310px;
    background: var(--card);
    border-radius: 22px;
    box-shadow: 0 10px 30px rgba(0,0,0,.45);
  }
  .card--front { left: 40px; top: 70px; }
  .card--back { left: 620px; top: 400px; }

  .brand { color: var(--teal); }
  .brand__name {
    font-weight: 700;
    line-height: 1;
    letter-spacing: 2px;
    display: flex;
    align-items: center;
    gap: 12px;
  }
  .brand__dot {
    border-radius: 50%;
    background: var(--teal);
    display: inline-block;
  }
  .brand__full {
    font-weight: 700;
    text-transform: uppercase;
    letter-spacing: 0.5px;
    line-height: 1.25;
    border-top: 1px solid var(--muted);
    padding-top: 6px;
    margin-top: 8px;
    white-space: nowrap;
  }

  .card--front .brand {
    position: absolute;
    left: 50%; top: 50%;
    transform: translate(-50%, -50%);
  }
  .card--front .brand__name { font-size: 84px; }
  .card--front .brand__dot { width: 18px; height: 18px; }
  .card--front .brand__full { font-size: 15px; }

  .card--back .brand {
    position: absolute;
    left: 40px; top: 80px;
  }
  .card--back .brand__name { font-size: 60px; }
  .card--back .brand__dot { width: 13px; height: 13px; }
  .card--back .brand__full { font-size: 11px; }

  .divider {
    position: absolute;
    left: 285px; top: 55px;
    width: 1px; height: 150px;
    background: var(--teal);
  }

  .contact {
    position: absolute;
    left: 305px; top: 66px;
    color: var(--text-soft);
    font-size: 13px;
    line-height: 1.35;
  }
  .contact__name {
    color: var(--teal);
    font-size: 19px;
    font-weight: 500;
    text-transform: uppercase;
    letter-spacing: 0.5px;
  }
  .contact__title { font-size: 13px; margin-bottom: 14px; }
  .contact__address { margin-bottom: 6px; }
  .contact__line { display: flex; align-items: center; gap: 7px; }
  .contact__icon { width: 14px; height: 14px; flex: none; }

  .tagline {
    position: absolute;
    left: 40px; bottom: 36px;
    color: var(--muted);
    font-size: 15px;
    letter-spacing: 2.2px;
    white-space: nowrap;
  }
</style>
</head>
<body>

  <section class="card card--front">
    <div class="brand">
      <div class="brand__name"><span class="brand__dot"></span>QLDR</div>
      <div class="brand__full">Harmonic Ladder<br>of Reasoning Matrix</div>
    </div>
  </section>

  <section class="card card--back">
    <div class="brand">
      <div class="brand__name"><span class="brand__dot"></span>QLDR</div>
      <div class="brand__full">Harmonic Ladder<br>of Reasoning Matrix</div>
    </div>

    <div class="divider"></div>

    <div class="contact">
      <div class="contact__name">Nora Pell</div>
      <div class="contact__title">Founder</div>
      <div class="contact__address">PO BOX 480 Harbour Lane<br>5th Avenue Ashford</div>
      <div class="contact__line">
        <svg class="contact__icon" viewBox="0 0 14 14" aria-hidden="true">
          <circle cx="7" cy="7" r="6.3" fill="none" stroke="#1ba7c1" stroke-width="1.2"/>
          <rect x="4.8" y="3.3" width="4.4" height="7.4" rx="0.8" fill="none" stroke="#1ba7c1" stroke-width="1"/>
        </svg>
        (204) 555-0187
      </div>
      <div class="contact__line">
        <svg class="contact__icon" viewBox="0 0 14 14" aria-hidden="true">
          <circle cx="7" cy="7" r="7" fill="#1ba7c1"/>
          <rect x="3.6" y="4.6" width="6.8" height="4.8" fill="none" stroke="#1c1e20" stroke-width="1"/>
          <path d="M3.6 4.6 L7 7.4 L10.4 4.6" fill="none" stroke="#1c1e20" stroke-width="1"/>
        </svg>
        hello@qldrmail.com
      </div>
    </div>

    <p class="tagline">Elevating Clarity for Purposeful Focused Leaders</p>
  </section>

</body>
</html>
```